Sprinkles & Tails 2nd Annual Fundraiser

I am a Realtor sponsoring the 2nd annual fundraiser on behalf of Allies of Harlow Vale Animal Haven. Like the flyer to be professional yet fun and inviting. Please see the attached file below. The 1st annual flyer was fun but not as professional, modern or inviting as I would have liked it to be.
Target Market(s)
Dog lovers in Ponte Vedra, Ponte Vedra Beach and Nocatee Florida
Logo Text
Needed
Font styles to use
Other font styles liked:
- Font that fits the style of the fundraiser
Colors
886aae
abd036
Requirements
Must have
- Please see the attached flyer and photos.
- This will be the 2nd Annual on Saturday, April 27, 2019 from 10AM - 1PM. Same location: Kendrick Realty, 418 Tillbrook Ave. Ponte Vedra FL 32075

```html
<!DOCTYPE html>
<html lang="en">
<head>
<meta charset="utf-8">
<title>Sprinkles and Tails Doggie Wash Extravaganza</title>
<link href="https://fonts.googleapis.com/css2?family=Chewy&family=Source+Sans+3:wght@400;600;700&display=swap" rel="stylesheet">
<style>
  :root {
    --purple: #886aae;
    --purple-deep: #5c2a91;
    --purple-dark: #4b1f7a;
    --green: #abd036;
    --lime: #a6e01e;
    --yellow: #fff200;
    --white: #ffffff;
    --ink-grey: #555555;
    --page: #ffffff;
  }
  * { margin: 0; padding: 0; box-sizing: border-box; }
  html, body { width: 1200px; height: 2757px; overflow: hidden; background: var(--page); }
  .flyer {
    position: absolute; left: 59px; top: 680px;
    width: 1082px; height: 1396px; overflow: hidden;
    background: var(--lime);
    box-shadow: 6px 8px 18px rgba(0,0,0,.35);
    font-family: "Source Sans 3", sans-serif;
  }
  .display-outline {
    font-family: "Chewy", "Comic Sans MS", cursive;
    font-weight: 400;
    color: var(--green);
    text-shadow:
      -2px -2px 0 var(--purple-deep), 2px -2px 0 var(--purple-deep),
      -2px 2px 0 var(--purple-deep), 2px 2px 0 var(--purple-deep),
      0 -3px 0 var(--purple-deep), 0 3px 0 var(--purple-deep),
      -3px 0 0 var(--purple-deep), 3px 0 0 var(--purple-deep),
      4px 5px 0 var(--purple-dark);
    white-space: nowrap;
    line-height: 1.05;
  }
  .hero-band { position: absolute; left: 0; top: 0; width: 1082px; height: 560px; }
  .title-card { position: absolute; left: 33px; top: 52px; width: 560px; height: 320px; }
  .title-card__frame {
    position: absolute; inset: -14px -10px; border: 4px solid var(--white);
    border-radius: 14px; transform: rotate(-4deg);
  }
  .title-card__panel { position: absolute; inset: 0; background: var(--yellow); border-radius: 10px; }
  .title-card__text {
    position: absolute; inset: 0; display: flex; flex-direction: column;
    align-items: center; justify-content: center; text-align: center;
  }
  .title-card__edition { font-size: 60px; }
  .title-card__edition sup { font-size: 32px; }
  .title-card__name { font-size: 60px; margin-top: 4px; }
  .title-card__event { font-size: 50px; margin-top: 6px; }
  .tagline {
    position: absolute; left: 164px; top: 409px; width: 440px; height: 55px;
    background: var(--green); border: 3px solid var(--purple-dark);
    border-radius: 6px; transform: rotate(-2deg);
    display: flex; align-items: center; justify-content: center;
    color: var(--purple-dark); font-weight: 700; font-size: 28px;
  }
  .hero-photo {
    position: absolute; left: 690px; top: 60px; width: 370px; height: 480px;
    background: radial-gradient(ellipse at 50% 42%, #8d8d8d, #555 58%, #c24a8a 82%, #6a3a9e 100%);
    border-radius: 45% 45% 30% 30%;
  }
  .org-badge {
    position: absolute; left: 324px; top: 491px; width: 200px; height: 200px;
    border-radius: 50%; background: var(--white);
    display: flex; align-items: center; justify-content: center; text-align: center;
    padding: 26px; color: #222; font-weight: 700; font-size: 22px; line-height: 1.15;
  }
  .event-photo {
    position: absolute; width: 266px; height: 266px; border-radius: 50%;
    border: 8px solid var(--purple-deep);
    background: linear-gradient(160deg, #b8b2a8, #6f6a73 55%, #9c8fa8);
  }
  .event-photo--one { left: 45px; top: 540px; }
  .event-photo--two { left: 200px; top: 676px; }
  .invite-note {
    position: absolute; left: 69px; top: 888px; width: 420px;
    color: var(--purple-deep); font-weight: 700; font-size: 22px; line-height: 1.3;
  }
  .date-card { position: absolute; left: 600px; top: 673px; width: 378px; height: 254px; }
  .date-card__shadow {
    position: absolute; left: 14px; top: 14px; right: -14px; bottom: -14px;
    background: var(--purple-deep); border-radius: 14px;
  }
  .date-card__panel {
    position: absolute; inset: 0; background: var(--yellow); border-radius: 14px;
    display: flex; flex-direction: column; align-items: center; text-align: center;
    padding-top: 24px; color: var(--purple-deep);
  }
  .date-card__day { font-size: 44px; margin-left: -110px; margin-right: -30px; }
  .date-card__time { font-size: 42px; margin-top: 6px; }
  .date-card__venue { font-weight: 700; font-size: 25px; line-height: 1.2; margin-top: 12px; }
  .highlights {
    position: absolute; left: 509px; top: 978px; width: 529px; height: 131px;
    list-style: none;
    background: var(--purple-deep); border-radius: 16px; color: var(--white);
    display: flex; flex-direction: column; align-items: center; justify-content: center;
    font-weight: 600; font-size: 21px; line-height: 1.5; text-align: center;
  }
  .donate-line {
    position: absolute; left: 0; right: 0; top: 1166px; text-align: center;
    color: var(--purple-deep); font-weight: 700; font-size: 25px;
  }
  .donate-line em { font-style: italic; }
  .contact {
    position: absolute; top: 1243px; color: var(--ink-grey);
    font-style: normal; font-size: 21px; line-height: 1.3;
  }
  .contact strong { color: var(--purple-deep); font-weight: 700; }
  .contact--sponsor { left: 233px; }
  .contact--charity { left: 751px; }
  .name-tile {
    position: absolute; left: 51px; top: 1251px; width: 164px; height: 94px;
    background: var(--white); border-radius: 10px;
    display: flex; align-items: center; justify-content: center; text-align: center;
    color: var(--purple-deep); font-weight: 700; font-size: 18px; line-height: 1.1; padding: 8px;
  }
  .name-disc {
    position: absolute; left: 610px; top: 1243px; width: 110px; height: 110px;
    border-radius: 50%; background: var(--white);
    display: flex; align-items: center; justify-content: center; text-align: center;
    color: #222; font-weight: 700; font-size: 12px; line-height: 1.1; padding: 12px;
  }
</style>
</head>
<body>
<main class="flyer">
  <svg class="hero-band" viewBox="0 0 1082 560" aria-hidden="true">
    <defs>
      <linearGradient id="heroPurple" x1="0" y1="0" x2="0" y2="1">
        <stop offset="0" stop-color="#8e55c9"/>
        <stop offset="1" stop-color="#5c2a91"/>
      </linearGradient>
    </defs>
    <rect x="0" y="0" width="1082" height="515" fill="url(#heroPurple)"/>
    <g fill="#5c2a91">
      <circle cx="0" cy="515" r="26"/><circle cx="54" cy="515" r="26"/><circle cx="108" cy="515" r="26"/>
      <circle cx="162" cy="515" r="26"/><circle cx="216" cy="515" r="26"/><circle cx="270" cy="515" r="26"/>
      <circle cx="324" cy="515" r="26"/><circle cx="378" cy="515" r="26"/><circle cx="432" cy="515" r="26"/>
      <circle cx="486" cy="515" r="26"/><circle cx="540" cy="515" r="26"/><circle cx="594" cy="515" r="26"/>
      <circle cx="648" cy="515" r="26"/><circle cx="702" cy="515" r="26"/><circle cx="756" cy="515" r="26"/>
      <circle cx="810" cy="515" r="26"/><circle cx="864" cy="515" r="26"/><circle cx="918" cy="515" r="26"/>
      <circle cx="972" cy="515" r="26"/><circle cx="1026" cy="515" r="26"/><circle cx="1080" cy="515" r="26"/>
    </g>
  </svg>

  <div class="hero-photo" role="img" aria-label="Photo of a smiling shaggy grey dog wearing a pink striped bandana"></div>

  <header class="title-card">
    <div class="title-card__frame"></div>
    <div class="title-card__panel"></div>
    <h1 class="title-card__text">
      <span class="title-card__edition display-outline">2<sup>nd</sup> Annual</span>
      <span class="title-card__name display-outline">Sprinkles and Tails</span>
      <span class="title-card__event display-outline">Doggie Wash<br>Extravaganza</span>
    </h1>
  </header>

  <p class="tagline">A Family Fun Event for All Ages</p>

  <div class="event-photo event-photo--one" role="img" aria-label="Photo of volunteers washing a dog at last year's event"></div>
  <div class="event-photo event-photo--two" role="img" aria-label="Photo of families with dogs at last year's event"></div>

  <div class="org-badge">Allies of Harlow Vale Animal Haven</div>

  <p class="invite-note">All domestic<br>breeds from<br>puppies to<br>seniors invited.<br>Please be sure<br>Furry Fido is tolerant of other dogs,<br>crowds and bathing.</p>

  <section class="date-card">
    <div class="date-card__shadow"></div>
    <div class="date-card__panel">
      <p class="date-card__day display-outline">Saturday, April 27, 2019</p>
      <p class="date-card__time display-outline">10 AM – 1 PM</p>
      <p class="date-card__venue">Kendrick Realty,<br>418 Tillbrook Ave.<br>Ponte Vedra FL 32075</p>
    </div>
  </section>

  <ul class="highlights">
    <li>• FREE Doggie Wash • Raffle Drawings</li>
    <li>• Food &amp; Beverages • Grand Prize</li>
    <li>• Vendors (FREE give-a-ways) • Donations Welcome</li>
  </ul>

  <p class="donate-line">To make a donation: https://www.socialpage.com/ahvah <em>(click : Donate)</em></p>

  <div class="name-tile">Marian Ostrow</div>
  <address class="contact contact--sponsor">
    <strong>Marian Ostrow</strong><br>Kendrick Realty Corp.<br>770.555.0192<br>marianostrow@kendrickrealtycorp.com
  </address>

  <div class="name-disc">Allies of Harlow Vale Animal Haven</div>
  <address class="contact contact--charity">
    <strong>Delia Brandt</strong><br>AHVAH<br>904.555.0147<br>delia-brandt@maildrop.net
  </address>
</main>
</body>
</html>
```